Harbormoor Property Institute Needs Banner Designs

I just launched an online real estate school at www.harbormoorpropertyinstitute.com

I am seeking designers to work on 2 banners (listed seperately) as well as a a Facebook design. This listing is for 1 of 2 banners.

First banner I intend to use on different job offering web sites. So "Launch your career into Real Estate" could be the concept. i'm open to 1 sentence pitch's. please look at my website to view graphics and colors.

```html
<!DOCTYPE html>
<html lang="en">
<head>
<meta charset="utf-8">
<title>Harbormoor Property Institute — Launch your career into Real Estate</title>
<link rel="stylesheet" href="https://fonts.googleapis.com/css2?family=Cormorant+Garamond:wght@500&family=Cormorant+SC:wght@700&family=Arimo:wght@700&display=swap">
<style>
  :root {
    --navy: #1f2a4e;
    --white: #ffffff;
    --sky-light: #eef8fc;
    --sky-mid: #bfe4f1;
    --sky-deep: #5fbcdc;
    --gold-top: #ffe15a;
    --gold-bottom: #f2a900;
    --gold-edge: #c98a00;
    --ink: #1a1a1a;
    --photo-sky: #9fb6c4;
    --photo-siding: #b9a88a;
    --photo-brick: #8a4a36;
  }
  * { margin: 0; padding: 0; box-sizing: border-box; }
  html, body { width: 1200px; height: 148px; overflow: hidden; background: var(--white); }

  .banner {
    position: relative;
    width: 1200px;
    height: 148px;
    overflow: hidden;
    background: var(--white);
  }

  .brand {
    position: absolute;
    left: 0; top: 0;
    width: 205px; height: 148px;
    display: flex;
    flex-direction: column;
    align-items: center;
    justify-content: center;
    gap: 8px;
    background: var(--white);
  }
  .brand-mark {
    width: 22px; height: 22px;
    background: var(--navy);
  }
  .brand-name {
    font-family: "Cormorant Garamond", serif;
    font-weight: 500;
    font-size: 21px;
    line-height: 1.05;
    color: var(--navy);
    text-align: center;
  }

  .pitch-field {
    position: absolute;
    left: 205px; top: 0;
    width: 690px; height: 148px;
    background: linear-gradient(90deg, var(--sky-light) 0%, var(--white) 30%, var(--sky-light) 55%, var(--sky-mid) 80%, var(--sky-deep) 100%);
  }

  .tagline {
    position: absolute;
    left: 305px; top: 22px;
    font-family: "Cormorant Garamond", serif;
    font-weight: 500;
    font-size: 32px;
    color: var(--navy);
    letter-spacing: 0.2px;
    white-space: nowrap;
  }
  .headline {
    position: absolute;
    left: 277px; top: 62px;
    font-family: "Cormorant SC", serif;
    font-weight: 700;
    font-size: 62px;
    line-height: 1;
    color: var(--navy);
    letter-spacing: 5px;
    white-space: nowrap;
  }
  .headline-rule {
    position: absolute;
    left: 293px; top: 127px;
    width: 350px; height: 0;
    border-top: 1.5px solid var(--navy);
  }

  .cta {
    position: absolute;
    left: 755px; top: 56px;
    width: 124px; height: 41px;
    border-radius: 5px;
    border: 1px solid var(--gold-edge);
    background: linear-gradient(180deg, var(--gold-top) 0%, var(--gold-bottom) 100%);
    box-shadow: 0 2px 3px rgba(0,0,0,0.25);
    display: flex;
    align-items: center;
    gap: 7px;
    padding-left: 8px;
    font-family: "Arimo", sans-serif;
    font-weight: 700;
    font-size: 18px;
    color: var(--ink);
    text-decoration: none;
  }
  .cta-icon { width: 18px; height: 18px; flex: none; }

  .house-photo {
    position: absolute;
    left: 890px; top: 0;
    width: 310px; height: 148px;
    background: linear-gradient(180deg, var(--photo-sky) 0%, var(--photo-siding) 55%, var(--photo-brick) 100%);
  }
</style>
</head>
<body>
  <div class="banner">
    <div class="brand">
      <span class="brand-mark"></span>
      <span class="brand-name">Harbormoor<br>Property Institute</span>
    </div>

    <div class="pitch-field"></div>

    <p class="tagline">Launch your career into</p>
    <h1 class="headline">Real Estate</h1>
    <span class="headline-rule"></span>

    <a class="cta" href="#">
      <svg class="cta-icon" viewBox="0 0 18 18" aria-hidden="true">
        <circle cx="9" cy="9" r="8.5" fill="#ffffff"/>
        <path d="M7 5 L12 9 L7 13 Z" fill="#e39a00"/>
      </svg>
      click here
    </a>

    <div class="house-photo" role="img" aria-label="Photo of a two-storey suburban house with brick and siding front"></div>
  </div>
</body>
</html>
```